Start Up Business Launcher needs a business card

We need a business card logo and word design for a new company called Varnick Ventures. We are a company dedicated to creating, testing, and developing, a myriad of repeatable and scalable business models (start ups) through innovative and consistent application of knowledge and expertise.

Target Market(s)

We test the marketability of start ups to various clientelle

Industry/Entity Type

Startup

Contact Information for Business Card

Varnick Ventures
Marcus Tellby LL.B, MBA.
Founder and President
#507 482 29 Ave SW Calgary AB
varnickventures@mailvista.example
(403) 821-3907

Colors

Designer to choose colors to be used in the design.

Requirements
Must have
• A logo for Varnick Ventures and a stylized written logo for Varnick Ventures
Nice to have
• bold design that demonstrates professionalism, consistency, and innovation.

```html
<!DOCTYPE html>
<html lang="en">
<head>
<meta charset="utf-8">
<title>Varnick Ventures – Business Card</title>
<link rel="stylesheet" href="https://fonts.googleapis.com/css2?family=Open+Sans:wght@400;600;700;800&display=swap">
<style>
  :root {
    --orange: #ff6600;
    --white: #ffffff;
    --ink: #1a1a1a;
    --backdrop: #e8e5e1;
  }
  * { margin: 0; padding: 0; box-sizing: border-box; }
  html, body { width: 1200px; height: 1200px; overflow: hidden; }
  body {
    background: var(--backdrop);
    font-family: "Open Sans", sans-serif;
    position: relative;
  }
  .card {
    position: absolute;
    left: 250px;
    width: 701px;
    height: 401px;
    box-shadow: 0 6px 18px rgba(0,0,0,0.18);
    overflow: hidden;
  }
  .card-front { top: 158px; background: var(--orange); }
  .card-back { top: 631px; background: var(--white); }

  .front-wordmark {
    position: absolute;
    inset: 0;
    display: flex;
    align-items: center;
    justify-content: center;
    gap: 14px;
    color: var(--white);
    font-weight: 700;
    font-size: 62px;
    letter-spacing: -1px;
    padding-bottom: 20px;
  }
  .wordmark-dot {
    width: 16px; height: 16px;
    background: var(--white);
    border-radius: 50%;
  }

  .holder { position: absolute; left: 41px; top: 52px; }
  .holder-name {
    color: var(--orange);
    font-size: 32px;
    font-weight: 400;
    line-height: 1.1;
    letter-spacing: -0.3px;
  }
  .holder-name .first { font-weight: 700; }
  .holder-title {
    color: var(--ink);
    font-size: 19px;
    line-height: 1.1;
  }
  .back-wordmark {
    position: absolute;
    right: 41px;
    top: 62px;
    color: var(--orange);
    font-weight: 700;
    font-size: 24px;
    letter-spacing: -0.4px;
  }

  .contact-panel {
    position: absolute;
    left: 41px;
    right: 41px;
    top: 155px;
    bottom: 0;
    background: var(--orange);
    display: flex;
    flex-direction: column;
    align-items: center;
    padding-top: 65px;
    gap: 12px;
  }
  .contact-row {
    display: flex;
    align-items: center;
    gap: 17px;
    color: var(--white);
    font-weight: 700;
    font-size: 19px;
    line-height: 24px;
  }
  .contact-icon {
    width: 22px; height: 22px;
    background: var(--white);
    flex: none;
  }
</style>
</head>
<body>
  <section class="card card-front">
    <div class="front-wordmark">Varnick Ventures<span class="wordmark-dot"></span></div>
  </section>

  <section class="card card-back">
    <div class="holder">
      <p class="holder-name"><span class="first">Marcus</span> Tellby LL.B, MBA.</p>
      <p class="holder-title">Founder and President</p>
    </div>
    <div class="back-wordmark">Varnick</div>

    <div class="contact-panel">
      <div class="contact-row">
        <svg class="contact-icon" viewBox="0 0 22 22" aria-hidden="true">
          <path d="M11 4a5 5 0 0 0-5 5c0 3.6 5 9 5 9s5-5.4 5-9a5 5 0 0 0-5-5z" fill="none" stroke="#ff6600" stroke-width="1.8"/>
          <circle cx="11" cy="9" r="1.8" fill="#ff6600"/>
        </svg>
        <span>#507 482 29 Ave SW Calgary AB</span>
      </div>
      <div class="contact-row">
        <svg class="contact-icon" viewBox="0 0 22 22" aria-hidden="true">
          <rect x="5" y="7" width="12" height="8" fill="#ff6600"/>
          <path d="M5 7l6 4.5L17 7" fill="none" stroke="#fff" stroke-width="1.2"/>
        </svg>
        <span>varnickventures@mailvista.example</span>
      </div>
      <div class="contact-row">
        <svg class="contact-icon" viewBox="0 0 22 22" aria-hidden="true">
          <path d="M7.5 5l2.2 3-1.3 1.5c.8 1.7 2.3 3.2 4 4l1.5-1.3 3 2.2-1.3 2.2C11 16.5 5.5 11 5.3 6.3z" fill="#ff6600"/>
        </svg>
        <span>(403) 821-3907</span>
      </div>
    </div>
  </section>
</body>
</html>
```